Bref créative
Environmental Company Bus Card
Kestrel Ecological Bus Card
Professional
Derek Malloy
Director of Operations
418 Fenwick Park Rd Suite B
Harwick, MD 21650
derek@kestrelecological.com
www.kestrelecological.com
I would like a fairly standard, but flashy/eye catching business card, with the logo and business name on the back of the card.
The card must have the required printing "bleed" around all edges. This wasn't done on the last project.
The logo shows the business name underneath of it. It does not have to be this way. The triangle logo can be the important feature, while the business name can be moved around wherever it is best suited.
Here is the logo file.
Here is the brochure file to see our color scheme and current design choice.

```html
<!DOCTYPE html>
<html lang="en">
<head>
<meta charset="utf-8">
<title>Kestrel Ecological Business Card</title>
<link href="https://fonts.googleapis.com/css2?family=Cinzel:wght@400;600;700&display=swap" rel="stylesheet">
<style>
  :root{
    --canvas:#2a2b2e;
    --card-black:#060708;
    --card-black-2:#16181b;
    --steel-deep:#12202c;
    --steel-mid:#2b4a60;
    --steel-light:#4f7690;
    --silver:#d9dde1;
    --silver-dim:#9aa3ab;
    --ink-light:#eef2f5;
  }
  *{box-sizing:border-box;margin:0;padding:0}
  html,body{width:1200px;height:874px;overflow:hidden}
  body{background:var(--canvas);font-family:"Cinzel",serif;position:relative}

  .card{position:absolute;width:540px;height:310px;border-radius:14px;overflow:hidden;
        box-shadow:0 10px 30px rgba(0,0,0,.45)}

  /* card back: brand side */
  .card--brand{left:40px;top:170px;
    background:radial-gradient(ellipse at 40% 35%,var(--card-black-2),var(--card-black) 70%)}
  .card--brand .mark{position:absolute;left:50%;top:78px;transform:translateX(-50%);
    width:70px;height:70px;border-radius:50%;
    background:linear-gradient(160deg,var(--steel-light),var(--steel-deep))}
  .card--brand .brand-name{position:absolute;left:0;right:0;top:178px;text-align:center;
    color:var(--silver);font-size:28px;font-weight:600;letter-spacing:1px;white-space:nowrap}

  /* card front: contact side */
  .card--contact{left:620px;top:400px;
    background:linear-gradient(150deg,var(--steel-light) 0%,var(--steel-mid) 35%,var(--steel-deep) 100%)}
  .card--contact svg.corner{position:absolute;inset:0}
  .card--contact .mark{position:absolute;right:52px;top:42px;width:56px;height:56px;border-radius:50%;
    background:linear-gradient(160deg,var(--steel-light),var(--steel-deep))}
  .contact-block{position:absolute;left:30px;top:72px;color:var(--ink-light);white-space:nowrap}
  .contact-block .company{font-size:17px;font-weight:600;letter-spacing:.8px;margin-bottom:14px}
  .contact-block .person{font-size:23px;font-weight:700;line-height:1}
  .contact-block .role{font-size:12px;color:var(--silver);margin:4px 0 12px}
  .contact-block .address{font-size:11px;line-height:1.45;color:var(--silver)}
  .details{position:absolute;left:300px;top:150px;list-style:none;color:var(--ink-light);font-size:11px;white-space:nowrap}
  .details li{display:flex;align-items:center;gap:7px;height:19px}
  .details svg{width:11px;height:11px;fill:var(--silver);flex:none}
</style>
</head>
<body>

<section class="card card--brand" aria-label="Card back">
  <div class="mark"></div>
  <div class="brand-name">Kestrel Ecological LLC</div>
</section>

<section class="card card--contact" aria-label="Card front">
  <svg class="corner" viewBox="0 0 540 310" preserveAspectRatio="none" aria-hidden="true">
    <path d="M300 0 H540 V150 C470 150 400 110 360 70 C335 45 315 20 300 0 Z" fill="#060708"/>
    <path d="M300 0 C315 20 335 45 360 70 C400 110 470 150 540 150" fill="none" stroke="#d9dde1" stroke-width="3"/>
    <path d="M0 310 C120 290 200 300 290 310 Z" fill="rgba(0,0,0,.18)"/>
  </svg>
  <div class="mark"></div>

  <div class="contact-block">
    <div class="company">Kestrel Ecological LLC</div>
    <div class="person">Derek Malloy</div>
    <div class="role">Director of Operations</div>
    <div class="address">418 Fenwick Park Rd Suite B<br>Harwick, MD 21650</div>
  </div>

  <ul class="details">
    <li><svg viewBox="0 0 10 10"><path d="M2 0h2l1 3-1.5 1a6 6 0 0 0 2.5 2.5L7 5l3 1v2a2 2 0 0 1-2 2A8 8 0 0 1 0 2a2 2 0 0 1 2-2z"/></svg>410-555-0142</li>
    <li><svg viewBox="0 0 10 10"><rect x="3" y="0" width="4" height="10" rx="1"/></svg>443-555-0187</li>
    <li><svg viewBox="0 0 10 10"><rect x="0" y="3" width="10" height="5" rx="1"/><rect x="2" y="0" width="6" height="3"/></svg>410-555-0163</li>
    <li><svg viewBox="0 0 10 10"><path d="M0 2h10v6H0z M0 2l5 3 5-3"/></svg>derek@kestrelecological.com</li>
    <li><svg viewBox="0 0 10 10"><circle cx="5" cy="5" r="5"/></svg>www.kestrelecological.com</li>
  </ul>
</section>

</body>
</html>
```